Brisq.io Landing Page Redesign Challenge - Help us pop and convert better!

** Update: We might not have been clear enough in our original messaging. We’re VERY open to changing the primary color from blue, we want a site that pops and has a good vibe for our audience (Creators, influencers). We originally chose blue as that is trust building, but I'd love to see some designs that show flare and flavor, with some really good contrasting colors with purple as a primary color... We'd love to see something in between https://quibbet.com and https://tandrel.app ... Again, our only caveat is orange cannot be a primary color because of a competitor.**

We built our current landing page fast — because TomVexley picked us to power the launch of his VaultTrials show on Streamora Plus and we had to be ready overnight.

You can read the case study here:
https://brisq.io/app/blog/2025/05/08/tomvexley-streamora-vault-trials-launch

Now that the dust has settled, we’re ready for a proper redesign — and we want to see your vision.

What we need:

A bold, vibrant color palette that feels fresh and fun — something that speaks to digital creators, influencers, and small businesses with 1–3 person marketing teams.

Our current main color is #3690C2, used by our mascot (Pip).

A full landing page redesign (desktop and mobile) in Figma that:

Clearly explains what Brisq.io does (link management + smart analytics for creators and marketers).

Builds trust and credibility using social proof and metrics.

Flows users toward conversion (signing up or starting a paid plan).

Is visually appealing and fun, without being overwhelming.

To submit:

Please send:

A hero section mockup.

Your proposed color palette (with hex codes).

A rough idea of how you’d structure the rest of the page.

The winning designer will deliver the full redesign in Figma.

BONUS: We’re considering inviting the winning designer to join our startup long-term, on a stock option package (no salary for now, we're building revenue first) as we grow what we believe will be the best link platform on the internet.

We're excited to see what you create!

*** GUIDANCE ***

Hero Section

Should include this Title and subtitle:

More Than a Short Link.
Brisq.io is your creative command center — shorten, track, and transform links that adapt over time.

Should include these bullet points are something close to it:

Unlimited links & QR codes
Link-in-bio + shortener, combined
Monitor Your Links
Conversion analytics included
Free trial — no card required

Trust Bar Text

30M+
Trusted by over 30 million people
1B+
Data points tracked — and counting
Real-time
Every click. Every view. Tracked in real-time

The rest of the text you can find on our current Landing Page at: https://brisq.io

Feel free to create a new account and play around with the site, to get screen shots and such.

Target Market(s)

Creators, Influencers and SMBs with 1-3 person marketing team

Industry/Entity Type

Social, Marketing

Number of Pages Required

1 page

Font styles to use
Other font styles liked:
• Logo is Belotta, Main text is Lato

Colors
0054AA
0677BA
7BADD7
CADEEF
E8F1F8
6B429C
8869AF
B7A5CE
E3DAEB
F3F0F8

Requirements
Must have
• Equivalent sections as my current page,
Nice to have
• Trust Bar - I have an example attached with my latest attempt to make the site look better.
Should not have
• Orange, our biggest competitor uses orange heavily.

```html
<!DOCTYPE html>
<html lang="en">
<head>
<meta charset="utf-8">
<title>Brisq.io — More Than a Short Link</title>
<link href="https://fonts.googleapis.com/css2?family=Lato:ital,wght@0,300;0,400;0,700;0,900;1,400&family=Poppins:wght@300;400;500;600&display=swap" rel="stylesheet">
<style>
:root{
  --purple:#6b429c;
  --purple-mid:#8869af;
  --purple-soft:#b7a5ce;
  --purple-pale:#e3daeb;
  --purple-wash:#f3f0f8;
  --blue-deep:#0054aa;
  --blue:#0677ba;
  --mascot:#3690c2;
  --blue-pale:#cadeef;
  --blue-wash:#e8f1f8;
  --ink:#1f1a2b;
  --muted:#5d566a;
  --line:#e6dfef;
}
*{box-sizing:border-box;margin:0;padding:0}
html,body{width:1200px;height:5181px;overflow:hidden}
body{position:relative;background:#fff;font-family:"Lato",sans-serif;color:var(--ink)}
.abs{position:absolute}
.btn{position:absolute;display:flex;align-items:center;justify-content:center;background:var(--purple);color:#fff;font-family:"Lato",sans-serif;font-weight:700;font-size:14px;border-radius:6px;box-shadow:0 2px 6px rgba(107,66,156,.25)}
.btn.alt{background:var(--blue-deep)}
.logo{font-family:"Poppins",sans-serif;font-weight:400;color:var(--purple);font-size:32px;letter-spacing:.5px}
.sec-title{position:absolute;left:0;width:1200px;text-align:center;color:var(--purple);font-size:26px;font-weight:900}
.sec-sub{position:absolute;left:0;width:1200px;text-align:center;color:var(--muted);font-size:13px}

.nav a{position:absolute;top:32px;font-size:14px;color:var(--ink);text-decoration:none}
.nav a.active{color:var(--purple);font-weight:700}

.hero-title{left:58px;top:200px;font-size:50px;line-height:56px;color:var(--purple);font-weight:900}
.hero-title span{color:var(--blue);font-weight:700}
.hero-sub{left:62px;top:324px;width:440px;font-size:14px;line-height:22px;color:#3a3346}
.ticks{left:62px;top:390px;list-style:none}
.ticks li{font-size:15px;font-weight:700;height:27px;display:flex;align-items:center;gap:10px;color:#2a2236}
.trust{top:640px;width:240px;text-align:center}
.trust b{display:block;font-size:28px;font-weight:900;color:var(--purple)}
.trust span{display:block;font-size:13px;color:var(--muted);line-height:19px;margin-top:4px}

.feat-card{position:absolute;top:1001px;width:131px;height:139px;background:#fff;border:1px solid var(--line);border-radius:8px;box-shadow:0 2px 8px rgba(107,66,156,.08);text-align:center}
.feat-card svg{margin-top:26px}
.feat-card p{font-size:14px;font-weight:700;line-height:18px;margin-top:8px}

.why{position:absolute}
.why h4{font-size:17px;font-weight:700;color:var(--ink)}
.why p{font-size:13px;color:var(--muted);line-height:20px;margin-top:8px}
.why.left{text-align:right}
.why-icon{position:absolute;width:60px;height:60px;border-radius:50%;background:var(--purple);display:flex;align-items:center;justify-content:center;box-shadow:0 0 0 4px var(--purple-pale)}

.case-card{left:648px;top:1912px;width:484px;height:266px;background:#fff;border:1px solid var(--purple-soft);border-radius:10px;box-shadow:0 6px 14px rgba(107,66,156,.18);text-align:center}

.arrow{position:absolute;width:40px;height:40px;border-radius:50%;background:var(--purple-pale);display:flex;align-items:center;justify-content:center}

.big-card{position:absolute;top:2851px;width:527px;height:446px;background:#fff;border:1px solid var(--line);border-radius:10px;box-shadow:0 2px 10px rgba(107,66,156,.08)}
.big-card h3{position:absolute;left:29px;top:260px;font-size:19px;font-weight:900}
.big-card p{position:absolute;left:29px;top:298px;width:400px;font-size:13px;line-height:20px;color:var(--muted)}

.ext{position:absolute;top:3590px;width:240px}
.ext .dot{position:absolute;left:24px;top:0;width:48px;height:48px;border-radius:50%;background:#fff;box-shadow:0 2px 6px rgba(0,0,0,.12)}
.ext .dot i{position:absolute;left:10px;top:10px;width:28px;height:28px;border-radius:50%}
.ext h4{position:absolute;left:84px;top:14px;font-size:17px;font-weight:700}
.ext p{position:absolute;left:24px;top:73px;width:210px;font-size:12.5px;line-height:20px;color:var(--muted)}

.faq{position:absolute;width:523px;height:38px;background:var(--purple-wash);border-radius:6px;display:flex;align-items:center;padding-left:20px;font-size:14px;color:#332b40}
.faq .pm{position:absolute;right:-8px;top:5px;width:28px;height:28px;border-radius:50%;background:var(--purple);color:#fff;font-size:20px;display:flex;align-items:center;justify-content:center;line-height:1}

.sec-card{position:absolute;top:4624px;width:346px;height:226px;background:#fff;border:1px solid var(--line);border-radius:10px;text-align:center}
.sec-card .badge{width:62px;height:62px;border-radius:50%;background:var(--purple);margin:20px auto 0;box-shadow:0 0 0 6px var(--purple-pale)}
.sec-card h4{font-size:17px;font-weight:700;margin-top:28px}
.sec-card p{font-size:13px;line-height:20px;color:var(--muted);margin:12px auto 0;width:260px}

.foot h5{position:absolute;top:5006px;font-size:16px;font-weight:900;color:var(--purple)}
.foot a{position:absolute;font-size:13px;color:#3a3346;text-decoration:none}
.social{position:absolute;top:5046px;width:34px;height:34px;border-radius:50%;border:2px solid var(--purple);background:#fff}
.mascot{background:linear-gradient(160deg,#5aa6d6,var(--mascot))}
</style>
</head>
<body>

<svg class="abs" style="left:0;top:0" width="1200" height="830" viewBox="0 0 1200 830" preserveAspectRatio="none" aria-hidden="true">
  <defs>
    <linearGradient id="heroG" x1="0" y1="0" x2="1" y2="1">
      <stop offset="0" stop-color="#ffffff"/>
      <stop offset=".45" stop-color="#f3f0f8"/>
      <stop offset="1" stop-color="#e3daeb"/>
    </linearGradient>
  </defs>
  <path d="M0 0H1200V760C1050 740 940 800 780 805 620 810 520 760 360 748 200 736 80 770 0 800Z" fill="url(#heroG)"/>
</svg>

<div class="abs logo" style="left:60px;top:18px">Brisq.io</div>
<nav class="nav">
  <a class="active" style="left:413px">Home</a>
  <a style="left:484px">Why Brisq.io</a>
  <a style="left:597px">Pricing</a>
  <a style="left:671px">Features</a>
  <a style="left:756px">Blog</a>
</nav>
<div class="btn alt" style="left:810px;top:22px;width:134px;height:40px">Quickpass Login</div>
<div class="btn" style="left:959px;top:22px;width:181px;height:40px">Start My Free Trial</div>

<h1 class="abs hero-title">More Than a<br><span>Short Link.</span></h1>
<p class="abs hero-sub">Brisq.io is your creative command center — shorten, track, and transform links that adapt over time.</p>
<ul class="abs ticks">
  <li><svg width="14" height="14" viewBox="0 0 14 14"><path d="M2 7l3 3 7-8" stroke="#6b429c" stroke-width="2.2" fill="none"/></svg>Unlimited links &amp; QR codes</li>
  <li><svg width="14" height="14" viewBox="0 0 14 14"><path d="M2 7l3 3 7-8" stroke="#6b429c" stroke-width="2.2" fill="none"/></svg>Link-in-bio + shortener, combined</li>
  <li><svg width="14" height="14" viewBox="0 0 14 14"><path d="M2 7l3 3 7-8" stroke="#6b429c" stroke-width="2.2" fill="none"/></svg>Monitor Your Links</li>
  <li><svg width="14" height="14" viewBox="0 0 14 14"><path d="M2 7l3 3 7-8" stroke="#6b429c" stroke-width="2.2" fill="none"/></svg>Conversion analytics included</li>
  <li><svg width="14" height="14" viewBox="0 0 14 14"><path d="M2 7l3 3 7-8" stroke="#6b429c" stroke-width="2.2" fill="none"/></svg>Free trial — no card required</li>
</ul>

<svg class="abs" style="left:597px;top:155px" width="543" height="384" viewBox="0 0 543 384" aria-label="Analytics dashboard preview">
  <rect width="543" height="384" rx="8" fill="#2b2633"/>
  <circle cx="503" cy="12" r="4" fill="#3fbf5a"/><circle cx="516" cy="12" r="4" fill="#e0c13a"/><circle cx="529" cy="12" r="4" fill="#d84a6a"/>
  <rect x="40" y="4" width="150" height="16" rx="3" fill="#4a4452"/>
  <text x="52" y="16" font-family="Lato,sans-serif" font-size="10" fill="#ddd">Brisq.io</text>
  <rect x="66" y="24" width="410" height="18" rx="3" fill="#4a4452"/>
  <text x="90" y="37" font-family="Lato,sans-serif" font-size="12" fill="#e6e6e6">https://brisq.io/app/analytics</text>
  <rect x="6" y="46" width="531" height="304" fill="#fff"/>
  <text x="200" y="62" font-family="Lato,sans-serif" font-size="6" fill="#777">Clicks over time</text>
  <path d="M14 110 L20 92 26 104 32 86 38 100 44 84 50 98 56 80 62 96 68 90 74 100 80 78 86 94 92 88 98 70 104 92 110 86 116 98 122 76 128 94 134 84 140 100 146 80 152 90 158 72 164 96 170 86 176 94 182 68 188 90 194 84 200 98 206 78 212 92 218 86 224 100 230 82 236 94 242 74 248 90 254 84 260 98 266 80 272 96 278 88 284 102 290 84 296 96 302 100 302 130 14 130Z" fill="#e3daeb"/>
  <path d="M14 110 L20 92 26 104 32 86 38 100 44 84 50 98 56 80 62 96 68 90 74 100 80 78 86 94 92 88 98 70 104 92 110 86 116 98 122 76 128 94 134 84 140 100 146 80 152 90 158 72 164 96 170 86 176 94 182 68 188 90 194 84 200 98 206 78 212 92 218 86 224 100 230 82 236 94 242 74 248 90 254 84 260 98 266 80 272 96 278 88 284 102 290 84 296 96 302 100" stroke="#6b429c" stroke-width="1.2" fill="none"/>
  <text x="404" y="78" font-family="Lato,sans-serif" font-size="7" fill="#6b429c">Browsers</text>
  <circle cx="400" cy="140" r="40" fill="none" stroke="#b7a5ce" stroke-width="14"/>
  <circle cx="400" cy="140" r="40" fill="none" stroke="#6b429c" stroke-width="14" stroke-dasharray="150 252"/>
  <circle cx="400" cy="140" r="40" fill="none" stroke="#0677ba" stroke-width="14" stroke-dasharray="40 252" stroke-dashoffset="-150"/>
  <g fill="#8869af"><rect x="480" y="80" width="6" height="4"/><rect x="480" y="90" width="6" height="4"/><rect x="480" y="100" width="6" height="4"/><rect x="480" y="110" width="6" height="4"/><rect x="480" y="120" width="6" height="4"/><rect x="480" y="130" width="6" height="4"/><rect x="480" y="140" width="6" height="4"/><rect x="480" y="150" width="6" height="4"/><rect x="480" y="160" width="6" height="4"/></g>
  <text x="180" y="190" font-family="Lato,sans-serif" font-size="6" fill="#555">Geographic distribution</text>
  <rect x="14" y="208" width="350" height="124" rx="2" fill="#f3f0f8" role="img" aria-label="World map of visitor locations"/>
  <text x="376" y="228" font-family="Lato,sans-serif" font-size="6" fill="#555">Top countries</text>
  <g fill="#6b429c"><rect x="382" y="248" width="140" height="5"/><rect x="382" y="258" width="60" height="5"/><rect x="382" y="268" width="40" height="5"/><rect x="382" y="278" width="30" height="5"/><rect x="382" y="288" width="24" height="5"/><rect x="382" y="298" width="18" height="5"/><rect x="382" y="308" width="14" height="5"/></g>
  <rect x="6" y="352" width="531" height="26" fill="#3a3442"/>
  <rect x="12" y="358" width="56" height="14" rx="2" fill="#5a5462"/>
</svg>

<div class="abs mascot" role="img" aria-label="Pip the raccoon mascot waving" style="left:450px;top:392px;width:186px;height:194px;border-radius:46% 46% 40% 40%"></div>

<div class="abs trust" style="left:240px"><b>30M+</b><span>Trusted by over 30<br>million people</span></div>
<div class="abs" style="left:479px;top:660px;width:1px;height:56px;background:var(--purple-soft)"></div>
<div class="abs trust" style="left:479px"><b>1B+</b><span>Data points tracked —<br>and counting</span></div>
<div class="abs" style="left:719px;top:660px;width:1px;height:56px;background:var(--purple-soft)"></div>
<div class="abs trust" style="left:720px"><b>Real-time</b><span>Every click. Every view.<br>Tracked in real-time</span></div>

<h2 class="sec-title" style="top:888px">Try Brisq.io Essentials FREE for 7 Days!</h2>
<p class="sec-sub" style="top:934px;line-height:21px">Experience premium features like Advanced Analytics, Geo Redirects, AI<br>Enhancements and more. No credit card required.</p>
<div class="feat-card" style="left:283px">
  <svg width="40" height="36" viewBox="0 0 40 36" fill="none" stroke="#6b429c" stroke-width="1.8"><rect x="4" y="22" width="6" height="12"/><rect x="14" y="16" width="6" height="18"/><rect x="24" y="10" width="6" height="24"/><path d="M4 14l10-6 8 4 14-10"/></svg>
  <p>Advanced<br>Analytics</p>
</div>
<div class="feat-card" style="left:449px">
  <svg width="40" height="36" viewBox="0 0 40 36" fill="none" stroke="#6b429c" stroke-width="1.8"><circle cx="20" cy="18" r="15"/><ellipse cx="20" cy="18" rx="7" ry="15"/><path d="M5 18h30M8 10h24M8 26h24"/></svg>
  <p>Geo<br>Redirects</p>
</div>
<div class="feat-card" style="left:614px">
  <svg width="40" height="36" viewBox="0 0 40 36" fill="none" stroke="#6b429c" stroke-width="1.8"><circle cx="20" cy="18" r="8"/><path d="M20 3v6M20 27v6M5 18h6M29 18h6M9 7l5 5M26 24l5 5M31 7l-5 5M14 24l-5 5"/></svg>
  <p>Ai<br>Enhancements</p>
</div>
<div class="feat-card" style="left:780px">
  <svg width="40" height="36" viewBox="0 0 40 36" fill="none" stroke="#6b429c" stroke-width="1.8"><rect x="6" y="3" width="28" height="8" rx="2"/><rect x="6" y="14" width="28" height="8" rx="2"/><path d="M12 25v8M28 25v8M12 33h16"/></svg>
  <p>Priority<br>Support</p>
</div>
<div class="btn alt" style="left:428px;top:1174px;width:151px;height:37px">Quickpass Login</div>
<div class="btn" style="left:587px;top:1174px;width:183px;height:37px">Start My Free Trial</div>

<h2 class="sec-title" style="top:1282px">Why Choose Us</h2>
<p class="sec-sub" style="top:1328px">Real solutions for real link management challenges</p>
<div class="abs" style="left:499px;top:1434px;width:200px;height:200px;border-radius:50%;border:2px solid var(--purple-soft);background:#fff;display:flex;align-items:center;justify-content:center"><span class="logo" style="font-size:30px">Brisq.io</span></div>

<div class="why left" style="left:80px;top:1390px;width:340px"><h4>Tired of Link Limits?</h4><p>While others cap you at 10–100 links<br>per month, we give you unlimited<br>links and QR codes.</p></div>
<div class="why-icon" style="left:440px;top:1390px"><svg width="30" height="30" viewBox="0 0 30 30" fill="none" stroke="#fff" stroke-width="2"><path d="M12 18l6-6M10 14l-3 3a4 4 0 006 6l3-3M20 16l3-3a4 4 0 00-6-6l-3 3"/></svg></div>

<div class="why left" style="left:40px;top:1518px;width:342px"><h4>Juggling Multiple Tools?</h4><p>Stop switching between Clipto and<br>Bioroot. Get powerful link<br>shortening.</p></div>
<div class="why-icon" style="left:402px;top:1518px"><svg width="30" height="30" viewBox="0 0 30 30" fill="none" stroke="#fff" stroke-width="2"><rect x="11" y="11" width="8" height="8"/><circle cx="5" cy="5" r="3"/><circle cx="25" cy="5" r="3"/><circle cx="5" cy="25" r="3"/><circle cx="25" cy="25" r="3"/><path d="M7 7l4 4M23 7l-4 4M7 23l4-4M23 23l-4-4"/></svg></div>

<div class="why left" style="left:80px;top:1646px;width:342px"><h4>Need Enterprise-Grade Security?</h4><p>Full SOC 2 Type II compliance,<br>GDPR ready, and battle-tested<br>DDoS protection.</p></div>
<div class="why-icon" style="left:442px;top:1646px"><svg width="30" height="30" viewBox="0 0 30 30" fill="none" stroke="#fff" stroke-width="2"><path d="M15 3l10 4v8c0 6-4 10-10 12C9 25 5 21 5 15V7z"/><path d="M10 15l4 4 6-7"/></svg></div>

<div class="why-icon" style="left:702px;top:1390px"><svg width="30" height="30" viewBox="0 0 30 30" fill="none" stroke="#fff" stroke-width="2"><rect x="4" y="5" width="22" height="18"/><path d="M8 19l5-6 4 3 5-7"/></svg></div>
<div class="why" style="left:784px;top:1390px;width:330px"><h4>Analytics Too Basic?</h4><p>Get premium analytics at<br>half the price of<br>competitors.</p></div>

<div class="why-icon" style="left:740px;top:1518px"><svg width="30" height="30" viewBox="0 0 30 30" fill="none" stroke="#fff" stroke-width="2"><circle cx="15" cy="15" r="11"/><path d="M9 19l4-8 8-2-4 8z"/></svg></div>
<div class="why" style="left:822px;top:1518px;width:330px"><h4>Missing Brand Control?</h4><p>Take full control of your brand with<br>custom domains, branded QR codes,<br>and personalized bio pages.</p></div>

<div class="why-icon" style="left:696px;top:1646px"><svg width="30" height="30" viewBox="0 0 30 30" fill="none" stroke="#fff" stroke-width="2"><circle cx="15" cy="15" r="5"/><path d="M15 3v4M15 23v4M3 15h4M23 15h4M6.5 6.5l3 3M20.5 20.5l3 3M23.5 6.5l-3 3M9.5 20.5l-3 3"/></svg></div>
<div class="why" style="left:780px;top:1646px;width:360px"><h4>Complex Setup Holding You Back?</h4><p>Get started in seconds with<br>our intuitive platform. No<br>technical expertise needed...</p></div>

<svg class="abs" style="left:0;top:1770px" width="1200" height="550" viewBox="0 0 1200 550" preserveAspectRatio="none" aria-hidden="true">
  <path d="M0 20C200 0 400 40 600 30 800 20 1000 0 1200 15V520C1000 540 850 500 650 515 450 530 250 500 0 530Z" fill="#f3f0f8"/>
</svg>
<h3 class="abs" style="left:60px;top:1918px;font-size:25px;font-weight:900;color:var(--purple)">Case Study</h3>
<p class="abs" style="left:62px;top:1960px;font-size:16px;font-weight:700;line-height:27px">How TomVexley Used Brisq.io to Launch<br>Vault Trials Globally</p>
<p class="abs" style="left:62px;top:2025px;font-size:13px;line-height:20px;color:var(--muted)">One of the biggest creators in the world used our<br>geo-targeted smart links to drive millions of fans to<br>Streamora Plus.</p>
<div class="btn" style="left:60px;top:2103px;width:141px;height:33px">Read More</div>

<div class="abs" style="left:660px;top:1892px;width:470px;height:250px;background:var(--purple-mid);border-radius:10px;transform:rotate(4deg)"></div>
<div class="abs case-card">
  <p style="margin-top:52px;font-size:13px;font-style:italic;color:var(--muted)">Case Study</p>
  <p style="margin-top:14px;font-size:27px;line-height:32px;color:var(--purple)">TomVexley used our link:</p>
  <p style="font-size:29px;line-height:34px;font-weight:900;color:var(--ink)">Here’s what happened next</p>
  <p style="margin:14px auto 0;width:340px;font-size:13px;line-height:19px;color:#332b40">From DDoS attacks to global fans, here’s how our platform helped deliver one of the biggest creator campaigns of the year.</p>
</div>
<div class="abs mascot" role="img" aria-label="Pip the raccoon mascot standing proudly" style="left:613px;top:2047px;width:106px;height:124px;border-radius:44% 44% 36% 36%"></div>

<h2 class="sec-title" style="top:2375px">Our Testimonials</h2>
<div class="abs" style="left:300px;top:2441px;width:600px;height:193px;background:#fff;border-radius:8px;box-shadow:0 2px 12px rgba(107,66,156,.12);text-align:center">
  <p style="margin:34px auto 0;width:480px;font-size:13px;font-style:italic;line-height:20px;color:#3a3346">Brisq.io has revolutionized how I drive traffic to my Craftmarket store. It’s an all-in-one tool that’s boosted my engagement and sales — I couldn’t recommend it more!</p>
  <p style="margin-top:12px;font-size:15px;font-weight:700">Mara Voskuijl</p>
  <p style="margin-top:2px;font-size:12.5px;color:var(--muted)">CEO @ VoskBoutique</p>
</div>
<div class="abs" role="img" aria-label="Customer portrait" style="left:569px;top:2604px;width:60px;height:60px;border-radius:50%;background:linear-gradient(160deg,#c9b6d9,#8869af);border:3px solid var(--purple)"></div>
<div class="arrow" style="left:199px;top:2519px"><svg width="14" height="14" viewBox="0 0 14 14"><path d="M9 2L4 7l5 5" stroke="#6b429c" stroke-width="2.2" fill="none"/></svg></div>
<div class="arrow" style="left:969px;top:2519px"><svg width="14" height="14" viewBox="0 0 14 14"><path d="M5 2l5 5-5 5" stroke="#6b429c" stroke-width="2.2" fill="none"/></svg></div>

<h2 class="sec-title" style="top:2739px">Powerful Features for Everyone</h2>
<p class="sec-sub" style="top:2784px">From individuals to enterprises, we’ve got you covered</p>

<div class="big-card" style="left:60px">
  <div class="abs" role="img" aria-label="Brisq.io app shown on three phones" style="left:12px;top:0;width:503px;height:238px;border-radius:10px 10px 0 0;background:linear-gradient(135deg,#b7a5ce,#f3f0f8 60%,#cadeef)"></div>
  <h3>Mobile-First Experience</h3>
  <p>Create, manage, and track your links on any device. Our responsive platform ensures you’re always in control of your links, wherever you are.</p>
  <div class="btn" style="left:29px;top:386px;width:142px;height:34px">Read More</div>
</div>
<div class="big-card" style="left:613px">
  <div class="abs" role="img" aria-label="Advanced analytics dashboard screen" style="left:12px;top:0;width:503px;height:238px;border-radius:10px 10px 0 0;background:linear-gradient(135deg,#8869af,#f3f0f8 40%,#e8f1f8)"></div>
  <h3>Advanced Analytics</h3>
  <p>Gain valuable insights with comprehensive analytics. Track clicks, understand your audience, and optimize.</p>
  <div class="btn" style="left:29px;top:386px;width:142px;height:34px">Read More</div>
</div>
<div class="abs mascot" role="img" aria-label="Pip the raccoon peeking over the card" style="left:82px;top:2770px;width:110px;height:82px;border-radius:48% 48% 20% 20%"></div>
<div class="abs mascot" role="img" aria-label="Pip the raccoon peeking over the card" style="left:1000px;top:2770px;width:110px;height:82px;border-radius:48% 48% 20% 20%"></div>

<svg class="abs" style="left:0;top:3370px" width="1200" height="590" viewBox="0 0 1200 590" preserveAspectRatio="none" aria-hidden="true">
  <defs><linearGradient id="extG" x1="0" y1="0" x2="0" y2="1"><stop offset="0" stop-color="#f3f0f8"/><stop offset="1" stop-color="#e3daeb"/></linearGradient></defs>
  <path d="M0 30C250 0 450 50 700 40 950 30 1080 0 1200 10V520C1000 560 800 510 600 540 400 570 200 520 0 560Z" fill="url(#extG)"/>
</svg>
<h2 class="sec-title" style="top:3463px">Browser Extensions</h2>
<p class="sec-sub" style="top:3507px">Shorten URLs directly from your browser</p>

<div class="ext" style="left:60px"><div class="dot"><i style="background:#8869af"></i></div><h4>Orbit</h4><p>Shorten URLs with a single click directly from Orbit. Access your Brisq.io dashboard and analytics without leaving your current tab.</p><div class="btn" style="left:24px;top:186px;width:152px;height:36px">Add to Orbit</div></div>
<div class="abs" style="left:325px;top:3580px;width:1px;height:240px;background:var(--purple-soft)"></div>
<div class="ext" style="left:333px"><div class="dot"><i style="background:#b7a5ce"></i></div><h4>Ember</h4><p>Quick and easy URL shortening from Ember. Generate QR codes and track analytics seamlessly while browsing.</p><div class="btn" style="left:24px;top:186px;width:152px;height:36px">Add to Ember</div></div>
<div class="abs" style="left:595px;top:3580px;width:1px;height:240px;background:var(--purple-soft)"></div>
<div class="ext" style="left:605px"><div class="dot"><i style="background:#0677ba"></i></div><h4>Tidewave</h4><p>Seamlessly shorten URLs in Tidewave. Perfect integration with your browser for quick access to all Brisq.io features.</p><div class="btn" style="left:24px;top:186px;width:152px;height:36px">Add to Tidewave</div></div>
<div class="abs" style="left:867px;top:3580px;width:1px;height:240px;background:var(--purple-soft)"></div>
<div class="ext" style="left:878px"><div class="dot"><i style="background:#7badd7"></i></div><h4>Compass</h4><p>Native Compass integration for desktop users. Shorten URLs and manage your links with its signature simplicity.</p><div class="btn" style="left:24px;top:186px;width:152px;height:36px">Add to Compass</div></div>

<h2 class="sec-title" style="top:4028px">Frequently Asked Questions</h2>
<p class="sec-sub" style="top:4072px">Everything you need to know about our pricing and features</p>

<div class="faq" style="left:60px;top:4126px">Which plan is right for me?<span class="pm">+</span></div>
<div class="faq" style="left:60px;top:4183px">Do you offer a free trial?<span class="pm">+</span></div>
<div class="faq" style="left:60px;top:4240px;height:90px;align-items:flex-start;flex-direction:column;padding-top:11px">
  <b style="font-weight:700;font-size:14px">What happens when I exceed my plan’s limits?</b>
  <span style="font-size:12.5px;line-height:19px;color:var(--muted);margin-top:10px;width:460px">Your existing links will continue to work, but you won’t be able to create new ones until the next billing cycle or upgrading your plan.</span>
  <span class="pm">−</span>
</div>
<div class="faq" style="left:60px;top:4353px">Can I cancel my subscription anytime?<span class="pm">+</span></div>
<div class="faq" style="left:60px;top:4409px">Do you offer refunds?<span class="pm">+</span></div>

<div class="faq" style="left:617px;top:4126px">What are your data privacy &amp; security policies?<span class="pm">+</span></div>
<div class="faq" style="left:617px;top:4183px">Do you offer discounts?<span class="pm">+</span></div>
<div class="faq" style="left:617px;top:4240px">What’s included in the free plan?<span class="pm">+</span></div>
<div class="faq" style="left:617px;top:4296px">How do I upgrade or downgrade my plan?<span class="pm">+</span></div>
<div class="faq" style="left:617px;top:4353px">Do you have a limit on the number of clicks?<span class="pm">+</span></div>
<div class="faq" style="left:617px;top:4409px">Can I use my own domain name? *<span class="pm">+</span></div>

<h2 class="sec-title" style="top:4520px">Enterprise-Grade Security</h2>
<p class="sec-sub" style="top:4564px;line-height:21px">Trusted by businesses worldwide. Your data, safeguarded<br>by industry-leading security standards.</p>
<div class="sec-card" style="left:60px"><div class="badge"></div><h4>SOC 2 Type II</h4><p>Our Nimbus-hosted infrastructure meets rigorous security, availability, and confidentiality standards.</p></div>
<div class="sec-card" style="left:427px"><div class="badge"></div><h4>GDPR Compliant</h4><p>Your privacy rights protected. Full compliance with EU data protection regulations.</p></div>
<div class="sec-card" style="left:794px"><div class="badge"></div><h4>CCPA Compliant</h4><p>California privacy standards met. Complete control over your personal data.</p></div>

<svg class="abs" style="left:0;top:4880px" width="1200" height="301" viewBox="0 0 1200 301" preserveAspectRatio="none" aria-hidden="true">
  <path d="M0 40C200 10 400 50 600 35 800 20 1000 0 1200 20V301H0Z" fill="#f3f0f8"/>
</svg>
<footer class="foot">
  <div class="abs logo" style="left:60px;top:5008px">Brisq.io</div>
  <h5 style="left:336px">Company</h5>
  <a style="left:336px;top:5045px">About Us</a>
  <a style="left:336px;top:5069px">Contact</a>
  <h5 style="left:609px">Legal</h5>
  <a style="left:609px;top:5045px">Privacy Policy</a>
  <a style="left:609px;top:5069px">Terms of Service</a>
  <h5 style="left:883px">Community</h5>
  <span class="social" style="left:883px" aria-label="Social profile"></span>
  <span class="social" style="left:923px" aria-label="Social profile"></span>
  <span class="social" style="left:963px" aria-label="Social profile"></span>
  <p class="abs" style="left:0;top:5130px;width:1200px;text-align:center;font-size:12.5px;color:#3a3346">© 2025 Brisq.io, Co. All rights reserved.</p>
</footer>

</body>
</html>
```